Business Card - high end, modern health care

Hey designers!

We need a double sided business card for the boutique, cutting edge physical therapy rehabilitation centre in Sydney's Northern Beaches.

With the most qualified physios in the area The Harbourline Motion Clinic does what other physiotherapy practices do not, we take our time with our patients giving them longer appointments, better physios and therefor faster results!

We guarantee that the service people receive at THMC will be unparalleled.

Hence we need a business card to reflect our modern, boutique, high end service. The final design needs to reflect that we are in a class of our own yet with the feel of beachside retreat.

Below I have attached our logo in both blue on white and white on blue. The exact colour is;
and the font that we have used in our logo is Tex Gyre Aventador.

I like the idea of the blue as the main colour as it is more eye catching and our signage onto the main road will be in this blue and in the interest of consistency across marketing the blue needs to be a part of the design. However I would appreciate a few designs onto a wooden background as this is a visual theme within the fitout of the practice.

The design needs to be of standard size (91x55mm).

Target Market(s)

We target people who have an end outcome in mind and those who have had poor experiences with other providers and ensure that everyone gets the care that they deserve with a premium service that is tailored to the individuals circumstances. As a premium service, the target market is highly educated, business and tech savvy with the additional target market of elderly people who have self funded their retirement and see value in paying for the best ongoing rehabilitation to maintain independence.

Industry/Entity Type

Physical Therapy

Contact Information for Business Card

Name, designation( Titled Musculoskeletal Physiotherapist... there will also be those in the company that have multiple designations ie 5 or 6 words long), phone number, email, facebook, instagram, address

Font styles to use
Sans Serif

Colors

Designer to choose colors to be used in the design.

Requirements
Must have
• Front - The logo as large as possible, blue or wooden theme, and all of the important details.
• Back - A blank space/lines on which to write appointment times (no "Appointment, date, time" etc.)
Nice to have
• facebook url
• logos for facebook and instagram
• Mini logos for the phone and email?

```html
<!DOCTYPE html>
<html lang="en">
<head>
<meta charset="utf-8">
<title>The Harbourline Motion Clinic – Business Card</title>
<link href="https://fonts.googleapis.com/css2?family=Raleway:wght@400;500;600&display=swap" rel="stylesheet">
<style>
  :root{
    --backdrop:#5b5978;
    --brand-blue:#0c57a6;
    --brand-blue-soft:rgba(255,255,255,0.14);
    --ink:#1a1a1a;
    --rule:#222;
    --dash:#777;
    --paper:#ffffff;
    --social-a:#1f8fd6;
    --social-b:#e0609a;
  }
  *{margin:0;padding:0;box-sizing:border-box}
  html,body{width:1200px;height:1000px;overflow:hidden}
  body{background:var(--backdrop);position:relative;font-family:'Raleway',Arial,sans-serif;color:var(--ink)}

  .card{position:absolute;width:657px;height:375px;overflow:hidden;box-shadow:4px 6px 14px rgba(0,0,0,.35)}
  .card--front{left:136px;top:78px;background:var(--brand-blue)}
  .card--back{left:437px;top:548px;background:var(--paper)}

  .front-ring{position:absolute;left:0;top:0}

  .brand{position:absolute;display:flex;align-items:center;gap:12px}
  .brand__dot{width:52px;height:52px;border-radius:50%;flex:none}
  .brand__name{font-weight:600;line-height:1.08;letter-spacing:.03em;text-transform:uppercase}
  .card--front .brand{left:48px;top:155px}
  .card--front .brand__dot{background:#fff}
  .card--front .brand__name{color:#fff;font-size:25px}

  .card--back .brand{left:362px;top:66px;gap:9px}
  .card--back .brand__dot{width:44px;height:44px;background:var(--brand-blue)}
  .card--back .brand__name{color:var(--brand-blue);font-size:19px}

  .person{position:absolute;left:44px;top:66px}
  .person__name{font-size:25.5px;font-weight:400;line-height:1.1}
  .person__name span{color:var(--brand-blue)}
  .person__title{font-size:14.6px;margin-top:7px}

  .rule{position:absolute;left:44px;width:571px;height:1px;background:var(--rule)}
  .rule--top{top:140px}
  .rule--bottom{top:229px}

  .contact{position:absolute;display:flex;align-items:center;gap:15px;font-size:17.5px}
  .contact svg{flex:none}
  .contact--phone{left:44px;top:159px}
  .contact--email{left:44px;top:190px}

  .social{position:absolute;display:flex;align-items:center;gap:8px;font-size:15px;color:#333}
  .social__dot{width:21px;height:21px;border-radius:50%}
  .social--profile{left:443px;top:160px}
  .social--profile .social__dot{background:var(--social-a)}
  .social--gallery{left:443px;top:192px}
  .social--gallery .social__dot{background:var(--social-b)}

  .address{position:absolute;left:44px;top:240px;font-size:15px}

  .write-lines{position:absolute;left:44px;top:300px}
</style>
</head>
<body>

<section class="card card--front" aria-label="Card front">
  <svg class="front-ring" width="657" height="375" viewBox="0 0 657 375" aria-hidden="true">
    <circle cx="463" cy="174" r="164" fill="none" stroke="var(--brand-blue-soft)" stroke-width="22"/>
  </svg>
  <div class="brand">
    <div class="brand__dot"></div>
    <div class="brand__name">The Harbourline<br>Motion Clinic</div>
  </div>
</section>

<section class="card card--back" aria-label="Card back">
  <div class="person">
    <div class="person__name">Name of <span>Person</span></div>
    <div class="person__title">Musculoskeletal Physiotherapist</div>
  </div>

  <div class="brand">
    <div class="brand__dot"></div>
    <div class="brand__name">The Harbourline<br>Motion Clinic</div>
  </div>

  <div class="rule rule--top"></div>

  <div class="contact contact--phone">
    <svg width="22" height="22" viewBox="0 0 22 22" aria-hidden="true">
      <circle cx="11" cy="11" r="9.8" fill="none" stroke="#111" stroke-width="1.8"/>
      <path d="M7.3 6.2c.5-.5 1.2-.4 1.5.1l1 1.6c.3.5.2 1-.2 1.3l-.6.5c.5 1.2 1.4 2.1 2.6 2.7l.5-.6c.3-.4.9-.5 1.3-.2l1.6 1c.5.3.6 1 .1 1.5l-.7.7c-.6.6-1.5.7-2.3.3-2.4-1.1-4.3-3-5.4-5.4-.4-.8-.2-1.7.3-2.3z" fill="#111"/>
    </svg>
    <span>612.480.3957</span>
  </div>
  <div class="contact contact--email">
    <svg width="22" height="14" viewBox="0 0 22 14" aria-hidden="true">
      <rect x="0" y="0" width="22" height="14" fill="#111"/>
      <path d="M1 1l10 7 10-7" fill="none" stroke="#fff" stroke-width="1.3"/>
    </svg>
    <span>hello@harbourlinemotion.com</span>
  </div>

  <div class="social social--profile"><div class="social__dot"></div><span>profile/name</span></div>
  <div class="social social--gallery"><div class="social__dot"></div><span>gallery_name</span></div>

  <div class="rule rule--bottom"></div>

  <div class="address">No.01, Adrs line 01, Adrs line 02, Street, City, Country.</div>

  <svg class="write-lines" width="580" height="46" viewBox="0 0 580 46" aria-hidden="true">
    <line x1="0" y1="5.5" x2="580" y2="5.5" stroke="var(--dash)" stroke-width="1.3" stroke-dasharray="7 5"/>
    <line x1="0" y1="41.5" x2="580" y2="41.5" stroke="var(--dash)" stroke-width="1.3" stroke-dasharray="7 5"/>
  </svg>
</section>

</body>
</html>
```